Web Design Project

Need a web design to be built by in-house team of developers. I need the look and feel of the site done ready for the developers to take over.

The site is a crowd funding site like www.pledgeloft.example. Our site will have all the main functions provided for on this site.
We are not looking for sophisticated investors, instead we are looking for people with an interest in investing but that need a lot of help and support through the process.

I have already obtained the logo. I attach it here.

I also want to have a coming soon page designed. I have sketched out what i want here and am uploading it in excel. this is obviously very basic and not what i will want for the main site.

colours should be light and accessible: blues, greens, yellows.

Site is to be fun and accessible.

site will have a lot of communication based aspects needed.

I am looking for a long term relationship with a designer to do this and to do many more things. I will have a lot of banners and desgin work to do here, and am looking ONLY for someone that can work on an ongoing basis (not full time, but a few hours a week).

I am also after an animation - basic 2 minute intro - not full animation, part powerpoint and part animation. I have made a separate tender for this, please quote me on it. I want the same person doing them all preferably....
Updates

Hi all

I am impressed with some of these designs. I have uploaded the wireframe of the coming soon page. 

I prefer the designs so far that are utilizing our little icons etc. 

obviously i understand you havent got root access or anything yet so are struggling to put them in, but its worth a try, some of the designs are using them well. 

i like bright colours. 

i would also show me how you are going to design other aspects eg chat box, forum page etc. 

Industry/Entity Type

Communication

Requirements
Must have
• the site will have all the functions of www.pledgeloft.example and www.venturibay.example.

```html
<!DOCTYPE html>
<html lang="en">
<head>
<meta charset="utf-8">
<title>Ideafield – Forum</title>
<link href="https://fonts.googleapis.com/css2?family=Arimo:wght@400;700&family=Crimson+Pro:wght@400;600&display=swap" rel="stylesheet">
<style>
:root{
  --header-top:#3a3a3a;
  --header-bottom:#1c1c1c;
  --brand:#ffffff;
  --brand-dot:#e8a82a;
  --orange:#f08c00;
  --orange-light:#f8a91e;
  --nav-top:#ffffff;
  --nav-bottom:#c6d3df;
  --nav-text:#1a1a2a;
  --nav-active:#e8851a;
  --panel-top:#5b8fc4;
  --panel-bottom:#274f7c;
  --panel-head:#2a5180;
  --row-dark:#c9d9ea;
  --row-light:#eaf1f9;
  --table-head:#1f4574;
  --table-text:#343434;
  --footer:#111111;
  --white:#ffffff;
}
*{margin:0;padding:0;box-sizing:border-box}
html,body{width:1200px;height:1159px;overflow:hidden;background:var(--white)}
body{font-family:"Arimo",Arial,sans-serif}
.page{position:relative;width:1200px;height:1159px;overflow:hidden}
.abs{position:absolute}

/* header */
.site-header{left:0;top:0;width:1200px;height:146px;background:linear-gradient(var(--header-top),var(--header-bottom))}
.brand-dot{left:30px;top:56px;width:36px;height:36px;border-radius:50%;background:var(--brand-dot)}
.brand-name{left:80px;top:52px;font-family:"Arimo",Arial,sans-serif;font-weight:400;font-size:36px;line-height:44px;color:var(--brand)}
.social{top:14px;width:42px;height:44px;border-radius:6px}
.social.one{left:1024px;background:#3b5c9c}
.social.two{left:1068px;background:#3aa4d8}
.social.three{left:1112px;background:#1e6a9a}
.chat-icon{left:798px;top:68px;width:58px;height:52px;border-radius:50%;background:radial-gradient(#d9a96a,#6b4a7a)}
.chat-label{left:863px;top:88px;font-size:18px;color:var(--white)}
.auth-btn{left:934px;top:74px;width:238px;height:44px;border-radius:6px;background:linear-gradient(var(--orange-light),var(--orange));display:flex;align-items:center;justify-content:center;color:var(--white);font-size:18px;gap:22px}

/* nav */
.main-nav{left:0;top:146px;width:1200px;height:56px;background:linear-gradient(var(--nav-top),var(--nav-bottom));display:flex;align-items:center;justify-content:center;font-size:15px;color:var(--nav-text)}
.main-nav span{padding:0 12px}
.main-nav .sep{padding:0 4px}
.main-nav .active{color:var(--nav-active)}

/* side panels */
.panel{left:28px;width:350px;border-radius:6px;background:linear-gradient(var(--panel-top),var(--panel-bottom))}
.video{top:212px;height:227px}
.video-screen{left:13px;top:13px;width:322px;height:177px;background:linear-gradient(#ffffff,#eef2f7);border-radius:8px}
.player{left:13px;top:200px;width:322px;height:16px;background:#d8d8d8;border-radius:2px}
.panel-title{left:10px;width:330px;height:50px;border-radius:6px;background:linear-gradient(#4f7fb2,var(--panel-head));color:var(--white);font-family:"Crimson Pro",serif;font-weight:600;font-size:23px;display:flex;align-items:center;justify-content:center}
.newsletter{top:454px;height:190px}
.news-input{left:30px;top:70px;width:278px;height:36px;background:#eef4fb;border-radius:4px}
.subscribe{left:104px;top:122px;width:142px;height:44px;border-radius:5px;background:linear-gradient(var(--orange-light),var(--orange));font-family:"Crimson Pro",serif;font-weight:600;font-size:19px;color:#1c1c1c;display:flex;align-items:center;justify-content:center}
.blog{top:658px;height:321px}
.blog-date{left:21px;font-size:14px;color:#f6c12c}
.blog-text{left:15px;width:325px;font-size:13.5px;line-height:21px;color:var(--white)}
.read-more{right:25px;font-size:14px;color:#f6c12c}
.blog-rule{left:15px;width:320px;border-top:1px dotted var(--white)}

/* forum tools */
.tool{top:222px;font-family:"Crimson Pro",serif;font-size:19px;color:#222;display:flex;align-items:center;gap:6px}
.tool i{display:inline-block;width:22px;height:22px;border-radius:50%}
.search-field{left:907px;top:264px;width:147px;height:20px;border:1px solid #999}
.search-btn{left:1058px;top:264px;width:97px;height:22px;border:1px solid #444;border-radius:3px;background:#eee;font-size:12px;display:flex;align-items:center;justify-content:center}

/* forum table */
.forum{left:394px;top:298px;width:795px;height:696px;border:1px solid #5c87b8;padding:6px 5px}
.forum table{width:784px;border-collapse:collapse;table-layout:fixed;font-family:"Crimson Pro",serif;color:var(--table-text)}
.forum th{height:44px;background:linear-gradient(#3e6597,var(--table-head));color:var(--white);font-size:19px;font-weight:600;border-right:2px solid var(--white)}
.forum th:first-child{text-align:left;padding-left:19px;font-size:21px}
.forum td{height:58.4px;border-right:2px solid var(--white);font-size:16px;text-align:center}
.forum td:first-child{text-align:left;padding-left:26px;font-size:17px;line-height:21px;white-space:nowrap;overflow:hidden}
.forum td:last-child{font-size:14.5px;text-align:left;padding-left:10px}
.forum tr:nth-child(odd) td{background:var(--row-dark)}
.forum tr:nth-child(even) td{background:var(--row-light)}

/* footer */
.footer-rule{left:0;top:1002px;width:1200px;height:13px;background:#777}
.site-footer{left:0;top:1015px;width:1200px;height:144px;background:linear-gradient(#2a2a2a,var(--footer))}
.pay-box{left:22px;top:1039px;width:391px;height:96px;background:var(--white)}
.pay-inner{left:20px;top:16px;width:354px;height:70px;border:1px solid #e0a040;background:#fbf3e2}
.pay-name{left:24px;top:0;font-family:"Arimo",sans-serif;font-weight:700;font-size:22px;color:#1f3e7a}
.card{top:36px;width:44px;height:26px;border-radius:3px}
.footer-links{left:642px;top:1057px;font-size:14.5px;color:var(--white);display:flex;gap:20px}
.copyright{left:680px;top:1104px;font-size:14.5px;color:var(--white)}
</style>
</head>
<body>
<div class="page">
  <header class="site-header abs">
    <div class="brand-dot abs"></div>
    <div class="brand-name abs">Ideafield</div>
    <div class="social one abs" role="img" aria-label="Social network link"></div>
    <div class="social two abs" role="img" aria-label="Social network link"></div>
    <div class="social three abs" role="img" aria-label="Social network link"></div>
    <div class="chat-icon abs" role="img" aria-label="Chat icon"></div>
    <div class="chat-label abs">Chat</div>
    <div class="auth-btn abs"><span>Log in</span><span>|</span><span>Sign up</span></div>
  </header>

  <nav class="main-nav abs">
    <span>HOME</span><span class="sep">|</span>
    <span>INVEST</span><span class="sep">|</span>
    <span>GET INVESMENT</span><span class="sep">|</span>
    <span>HOW T WORKS</span><span class="sep">|</span>
    <span>ABOUT US</span><span class="sep">|</span>
    <span>BLOG</span><span class="sep">|</span>
    <span class="active">FORUM</span><span class="sep">|</span>
    <span>CONTACT US</span>
  </nav>

  <aside>
    <div class="panel video abs">
      <div class="video-screen abs" role="img" aria-label="Intro video preview frame"></div>
      <div class="player abs">
        <svg width="322" height="16"><rect x="3" y="3" width="10" height="10" fill="#333"/><rect x="18" y="4" width="14" height="8" fill="#555"/><line x1="80" y1="8" x2="300" y2="8" stroke="#888" stroke-width="2"/><circle cx="84" cy="8" r="4" fill="#555"/><rect x="305" y="4" width="12" height="8" fill="#333"/></svg>
      </div>
    </div>

    <div class="panel newsletter abs">
      <div class="panel-title abs" style="top:0">Newsletter</div>
      <div class="news-input abs"></div>
      <div class="subscribe abs">Subscribe</div>
    </div>

    <div class="panel blog abs">
      <div class="panel-title abs" style="top:10px">Latest from our blog</div>
      <div class="blog-date abs" style="top:80px">26.07.2011</div>
      <div class="blog-text abs" style="top:102px">It easily with new website widgetWe're pleased to announce our latest development to our website</div>
      <div class="read-more abs" style="top:162px">readmore</div>
      <div class="blog-rule abs" style="top:190px"></div>
      <div class="blog-date abs" style="top:212px">28.07.2011</div>
      <div class="blog-text abs" style="top:235px">It easily with new website widgetWe're pleased to announce our latest development to our website</div>
      <div class="read-more abs" style="top:295px">readmore</div>
    </div>
  </aside>

  <main>
    <div class="tool abs" style="left:702px"><i style="background:#7fb0dd"></i>Search</div>
    <div class="tool abs" style="left:814px"><i style="background:#7fae4a"></i>Memberlist</div>
    <div class="tool abs" style="left:955px"><i style="background:#c9504a"></i>Register</div>
    <div class="tool abs" style="left:1076px"><i style="background:#5a7fb0"></i>Login</div>
    <div class="search-field abs"></div>
    <div class="search-btn abs">Search Forums</div>

    <div class="forum abs">
      <table>
        <colgroup><col style="width:405px"><col style="width:131px"><col style="width:112px"><col style="width:136px"></colgroup>
        <thead><tr><th>Forum</th><th>Topics</th><th>Posts</th><th>Last Post</th></tr></thead>
        <tbody>
          <tr><td>News &amp; Announcements<br>Nodeforge Community news and announcements.</td><td>152</td><td>260</td><td>Sun, May 25 , 2010</td></tr>
          <tr><td>Testimonials<br>Help spread the world! Post your Jobs</td><td>177</td><td>336</td><td>Thu, May 28 , 2010</td></tr>
          <tr><td>Website Issues<br>Report problems with the nodeforge.example site.</td><td>152</td><td>156</td><td>Sun, May 25 , 2010</td></tr>
          <tr><td>Wiki Issues<br>Discuss Wiki Problems /Issues</td><td>158</td><td>260</td><td>Sun, Dec 25 , 2010</td></tr>
          <tr><td>News &amp; Announcements<br>Nodeforge Community news and announcements.</td><td>152</td><td>100</td><td>Sun, May 25 , 2010</td></tr>
          <tr><td>Jobs at Crimson Cap<br>Do you want to feel the air under your wings?</td><td>117</td><td>405</td><td>Sun, Sep 20 , 2010</td></tr>
          <tr><td>News &amp; Announcements<br>Nodeforge Community news and announcements.</td><td>152</td><td>147</td><td>Sun, May 25 , 2010</td></tr>
          <tr><td>Nodeforge Portal Users<br>User questions and comments about Portal.</td><td>165</td><td>200</td><td>Fri, May 10 , 2010</td></tr>
          <tr><td>News &amp; Announcements<br>Nodeforge Community news and announcements.</td><td>45</td><td>260</td><td>Sun, May 25 , 2010</td></tr>
          <tr><td>Nodeforge Portal Documentation<br>Discuss the Nodeforge Portal Documentation.</td><td>86</td><td>120</td><td>Wed, Aug 25 , 2010</td></tr>
          <tr><td>News &amp; Announcements<br>Nodeforge Community news and announcements.</td><td>59</td><td>260</td><td>Sun, May 25 , 2010</td></tr>
        </tbody>
      </table>
    </div>
  </main>

  <div class="footer-rule abs"></div>
  <footer class="site-footer abs"></footer>
  <div class="pay-box abs">
    <div class="pay-inner abs">
      <div class="pay-name abs">Paywell</div>
      <div class="card abs" style="left:8px;background:#c8463c"></div>
      <div class="card abs" style="left:62px;background:#3a5aa8"></div>
      <div class="card abs" style="left:116px;background:#e6e6e6"></div>
      <div class="card abs" style="left:170px;background:#2b4c9a"></div>
      <div class="card abs" style="left:224px;width:32px;background:#5c9bd6"></div>
      <div class="card abs" style="left:266px;width:78px;background:#f2f2f2;border:1px solid #999"></div>
    </div>
  </div>
  <div class="footer-links abs"><span>Privacy Policy</span><span>|</span><span>Terms &amp; Conditions</span><span>|</span><span>Contact Us</span></div>
  <div class="copyright abs">Copyright 2011 Ideafield ,&nbsp; All Rights Reserved</div>
</div>
</body>
</html>
```